Corwick Habitat Web

We just need an update/re-design of our existing web site that would include our new company logo and some new photo's. Our current web site can be viewed at www.corwickhabitat.com.au. We would require something very similar to what we have at the moment in terms of content it should all be the same.
The web site would basically act more as a portfolio than one that would generate more business.
We are after a very modern and simple design and maybe something where we can upload our own project photo's and project descriptions as we complete them.

Industry/Entity Type

It Company

```html
<!DOCTYPE html>
<html lang="en">
<head>
<meta charset="utf-8">
<title>Corwick Habitat</title>
<link rel="stylesheet" href="https://fonts.googleapis.com/css2?family=Raleway:wght@300;400;500&display=swap">
<style>
:root{
  --teal:#2c7f7b;
  --teal-veil:rgba(44,127,123,.78);
  --ink:#3f4145;
  --muted:#9a9a9a;
  --nav:#8a8a8a;
  --rule:#ececec;
  --footer:#333438;
  --sky:#c9ccce;
  --concrete:#7d8083;
  --slate:#3b4350;
}
*{box-sizing:border-box;margin:0;padding:0}
html,body{width:1017px;height:1200px;overflow:hidden;background:#fff;font-family:"Raleway",sans-serif}
.page{position:relative;width:1017px;height:1200px}
.wrap{position:absolute;left:136px;width:744px}

.site-header{top:20px;height:46px;display:flex;justify-content:space-between;align-items:center}
.brand{font-weight:300;font-size:27px;color:var(--ink);letter-spacing:.2px;white-space:nowrap}
.nav{display:flex;align-items:center;font-size:9.5px;font-weight:400;color:var(--nav)}
.nav a{color:inherit;text-decoration:none}
.nav .sep{margin:0 19px}

.hero{top:94px;height:286px;display:flex;gap:10px}
.hero .shot{flex:1}

.shot{position:relative}
.shot.a{background:linear-gradient(170deg,var(--sky) 0%,#b7babd 38%,var(--concrete) 62%,#2f3236 100%)}
.shot.b{background:linear-gradient(160deg,#d4d6d8 0%,#a9acaf 40%,#6e7175 70%,#2e3033 100%)}
.shot.c{background:linear-gradient(180deg,#8a8e92 0%,#c08a5a 45%,#8b8d90 70%,#55575a 100%)}
.shot.d{background:linear-gradient(170deg,#5d8fc4 0%,#9ab6cf 40%,#4a5158 75%,#2a2c2f 100%)}
.shot.e{background:linear-gradient(170deg,#e2e4e6 0%,#4b5462 35%,var(--slate) 75%,#26292d 100%)}
.shot.f{background:linear-gradient(180deg,#6a7e8a 0%,#c9cdd0 60%,#9aa0a3 100%)}
.shot.hover::after{content:"";position:absolute;inset:0;background:var(--teal-veil)}
.zoom{position:absolute;z-index:1;left:50%;top:50%;width:27px;height:27px;margin:-13.5px 0 0 -13.5px;border:1px solid #fff;display:flex;align-items:center;justify-content:center}

.intro{top:440px;display:flex;gap:20px}
.col{width:362px}
.col.right{width:362px}
.h2{font-size:15.5px;font-weight:400;color:var(--ink);line-height:20px}
.bar{width:38px;height:2px;background:var(--teal);margin:12px 0 20px}
.copy{font-size:10.3px;font-weight:400;color:var(--muted);line-height:15.3px}
.copy p+p{margin-top:15px}
.divider{height:1px;background:var(--rule);margin:28px 0 29px}
.thumbs{display:flex;justify-content:space-between}
.thumbs .shot{width:108px;height:108px}

.recent{top:759px}
.recent .bar{margin-bottom:19px}
.gallery{display:flex;justify-content:space-between}
.gallery .shot{width:172px;height:127px}
.pager{display:flex;justify-content:flex-end;gap:7px;margin-top:13px}
.pager span{width:20px;height:20px;border:1px solid var(--ink);display:flex;align-items:center;justify-content:center}

.site-footer{position:absolute;left:0;top:1038px;width:1017px;height:128px;background:var(--footer)}
.site-footer .inner{position:absolute;left:136px;top:32px;width:744px;height:46px;display:flex;justify-content:space-between;align-items:center}
.site-footer .brand{color:#fff}
.site-footer .nav{color:#fff}

.legal{top:1166px;height:34px;display:flex;justify-content:space-between;align-items:center}
.legal small{font-size:8px;color:var(--nav)}
.social{display:flex;gap:9px}
.social span{width:21px;height:21px;border:1px solid var(--ink)}
</style>
</head>
<body>
<div class="page">

  <header class="wrap site-header">
    <div class="brand">Corwick Habitat</div>
    <nav class="nav">
      <a href="#">Home</a><span class="sep">/</span>
      <a href="#">Recent Projects</a><span class="sep">/</span>
      <a href="#">Our Services</a><span class="sep">/</span>
      <a href="#">Contact Us</a>
    </nav>
  </header>

  <section class="wrap hero">
    <div class="shot a" role="img" aria-label="Photo of a modern office building facade with louvres under a cloudy sky"></div>
    <div class="shot b" role="img" aria-label="Photo of a cantilevered grey building wing seen from below"></div>
    <div class="shot f hover" role="img" aria-label="Photo of a fitted-out office interior corridor with patterned carpet">
      <span class="zoom"><svg width="11" height="11" viewBox="0 0 12 12"><circle cx="5" cy="5" r="3.6" fill="none" stroke="#fff" stroke-width="1.6"/><line x1="7.6" y1="7.6" x2="11" y2="11" stroke="#fff" stroke-width="1.8"/></svg></span>
    </div>
  </section>

  <section class="wrap intro">
    <div class="col">
      <h2 class="h2">Corwick Habitat Pty Ltd</h2>
      <div class="bar"></div>
      <p class="copy">Corwick Habitat Pty Ltd was established in 2005 and has been operating in the Sydney area, but has completed numerous projects<br>outside of Sydney.</p>
      <div class="divider"></div>
      <div class="thumbs">
        <div class="shot c" role="img" aria-label="Photo of a building with timber and grey cladding"></div>
        <div class="shot d" role="img" aria-label="Photo of a glazed office facade under a blue sky"></div>
        <div class="shot e" role="img" aria-label="Photo of a dark blue panelled building corner"></div>
      </div>
    </div>
    <div class="col right">
      <h2 class="h2">We specialise in the internal fit outs to</h2>
      <div class="bar"></div>
      <div class="copy">
        <p>- Industrial Offices<br>- Multi Storey Offices<br>- Commercial Projects<br>- Residential Houses<br>- External Facades</p>
        <p>The key group of our operating staff have all been involved in the construction industry for well over 20 years.</p>
        <p>Our employees are skilled and trained and have the experience to deliver the best possible product, safely and on time.</p>
        <p>At Corwick Habitat we pride ourselves on working together with our clients in providing the best possible service on schedule and within budget.</p>
      </div>
    </div>
  </section>

  <section class="wrap recent">
    <h2 class="h2">Recent Projects</h2>
    <div class="bar"></div>
    <div class="gallery">
      <div class="shot a" role="img" aria-label="Project photo of an office building facade with louvres"></div>
      <div class="shot c" role="img" aria-label="Project photo of a building with timber and grey cladding"></div>
      <div class="shot d hover" role="img" aria-label="Project photo of a glazed office facade">
        <span class="zoom"><svg width="11" height="11" viewBox="0 0 12 12"><circle cx="5" cy="5" r="3.6" fill="none" stroke="#fff" stroke-width="1.6"/><line x1="7.6" y1="7.6" x2="11" y2="11" stroke="#fff" stroke-width="1.8"/></svg></span>
      </div>
      <div class="shot e" role="img" aria-label="Project photo of a dark blue panelled building"></div>
    </div>
    <div class="pager">
      <span><svg width="8" height="10" viewBox="0 0 8 10"><polyline points="6,1 2,5 6,9" fill="none" stroke="#3f4145" stroke-width="1.6"/></svg></span>
      <span><svg width="8" height="10" viewBox="0 0 8 10"><polyline points="2,1 6,5 2,9" fill="none" stroke="#3f4145" stroke-width="1.6"/></svg></span>
    </div>
  </section>

  <footer class="site-footer">
    <div class="inner">
      <div class="brand">Corwick Habitat</div>
      <nav class="nav">
        <a href="#">Home</a><span class="sep">/</span>
        <a href="#">Recent Projects</a><span class="sep">/</span>
        <a href="#">Our Services</a><span class="sep">/</span>
        <a href="#">Contact Us</a>
      </nav>
    </div>
  </footer>

  <div class="wrap legal">
    <small>© Copyright Corwick Habitat Pty Ltd 2014</small>
    <div class="social" aria-label="Social links">
      <span></span><span></span><span></span>
    </div>
  </div>

</div>
</body>
</html>
```